Patternmaking service (fashion) card design

I need cards for my patternmaking service. I service both large and small fashion labels including ladies,mens and childrenswear. I would like cards that have a sort of vintage feel, especially 50's and 60's style. Pink is my signature colour. Its important to have a fashion reference of some kind.

Industry/Entity Type

Fashion

Contact Information for Business Card

Marigold Thimble, Patternmaking Service, Kessa Vantorin,
27 Pellham Lane. Ashbrook Vale. VIC. 3152. 0415836204, email:lacebird4@mailnest.example. "By appointment only"

```html
<!DOCTYPE html>
<html lang="en">
<head>
<meta charset="utf-8">
<title>Marigold Thimble – Patternmaking Service Card</title>
<link rel="stylesheet" href="https://fonts.googleapis.com/css2?family=Lobster&family=Libre+Franklin:wght@400&display=swap">
<style>
  :root {
    --page-bg: #efe9ea;
    --band-top: #e2559b;
    --band-top-deep: #d4478c;
    --body-pink: #c9307c;
    --body-pink-deep: #b8266f;
    --ink-light: #ffffff;
    --stitch: rgba(255, 255, 255, 0.75);
    --title-shadow: rgba(90, 10, 50, 0.45);
  }
  * { margin: 0; padding: 0; box-sizing: border-box; }
  html, body {
    width: 1200px; height: 900px; overflow: hidden;
    background: var(--page-bg);
  }
  .card {
    position: absolute;
    left: 220px; top: 220px;
    width: 760px; height: 460px;
    overflow: hidden;
    color: var(--ink-light);
    box-shadow: 0 6px 18px rgba(0, 0, 0, 0.18);
  }
  .header-band {
    position: absolute; left: 0; top: 0; width: 100%; height: 192px;
    background: linear-gradient(180deg, var(--band-top) 0%, var(--band-top-deep) 100%);
  }
  .body-field {
    position: absolute; left: 0; top: 192px; width: 100%; height: 268px;
    background: linear-gradient(180deg, var(--body-pink) 0%, var(--body-pink-deep) 100%);
  }
  .stitch-line {
    position: absolute; left: 0; top: 180px; width: 100%;
    border-top: 2px dashed var(--stitch);
  }
  .brand {
    position: absolute; left: 58px; top: 36px;
    font-family: "Lobster", cursive;
    text-shadow: 0 2px 3px var(--title-shadow);
    line-height: 1.1;
  }
  .brand-name { font-size: 54px; font-weight: 400; }
  .brand-service { font-size: 36px; font-weight: 400; margin-top: 2px; }
  .contact {
    font-family: "Libre Franklin", sans-serif;
    font-weight: 400;
  }
  .person-name {
    position: absolute; left: 58px; top: 224px;
    font-size: 33px;
  }
  .availability {
    position: absolute; right: 52px; top: 234px;
    font-size: 22px;
  }
  .details {
    position: absolute; left: 58px; top: 292px;
    list-style: none;
    font-size: 24px;
  }
  .details li {
    display: flex; align-items: center;
    height: 38px;
  }
  .details svg { width: 20px; height: 20px; margin-right: 16px; flex: none; fill: var(--ink-light); }
</style>
</head>
<body>
  <article class="card">
    <div class="header-band" role="img" aria-label="Decorative retro arch and diamond pattern in light pink tones"></div>
    <div class="body-field" role="img" aria-label="Decorative retro arch pattern in deep pink tones"></div>
    <div class="stitch-line"></div>

    <header class="brand">
      <h1 class="brand-name">Marigold Thimble</h1>
      <p class="brand-service">Patternmaking Service</p>
    </header>

    <p class="contact person-name">Kessa Vantorin</p>
    <p class="contact availability">By appointment only</p>

    <ul class="contact details">
      <li>
        <svg viewBox="0 0 20 20" aria-hidden="true"><path d="M4 1.5l3 .5 1.5 4-2 1.5c1 2.3 2.7 4 5 5l1.5-2 4 1.5.5 3c0 1.5-1.5 2.5-3 2.5C8 17.5 2.5 12 2.5 4.5c0-1.5 1-3 1.5-3z"/></svg>
        0415836204
      </li>
      <li>
        <svg viewBox="0 0 20 20" aria-hidden="true"><path d="M1 4h18v2l-9 6-9-6z"/><path d="M1 8l9 6 9-6v8H1z"/></svg>
        lacebird4@mailnest.example
      </li>
      <li>
        <svg viewBox="0 0 20 20" aria-hidden="true"><path d="M10 1l9 8h-3v9H4V9H1z"/><rect x="8" y="11" width="4" height="7" fill="#c9307c"/></svg>
        27 Pellham Lane, Ashbrook Vale. VIC 3152
      </li>
    </ul>
  </article>
</body>
</html>
```